TRK Kestrel Info Postcatd

I am looking for a beach volleyball doubles flyer that we can hand out to customers that gives some basic information about our outdoor doubles training program. We want this to be a high performance program. We offer training from May until August. The cost of the program is $500. We are going to take no more than 16 players to train. Players must be serious to attend tryouts. Tryouts will be April 5th. We want serious players interested in training and competing at a high level. Season is from April (tryouts) to August 10. Uniform, tournament entry fees are covered, travel is not covered. Our website is trkkestrel.com

Industry/Entity Type

Training

```html
<!DOCTYPE html>
<html lang="en">
<head>
<meta charset="utf-8">
<title>TRK Kestrel – Beach Doubles Postcard</title>
<link rel="stylesheet" href="https://fonts.googleapis.com/css2?family=Source+Sans+3:ital,wght@0,400;0,600;0,700;1,400&family=Dancing+Script:wght@600&display=swap">
<style>
  :root {
    --ink: #1a1a1a;
    --paper: #ffffff;
    --band: #000000;
    --sun-light: #fdf3c8;
    --sun-gold: #f2c25a;
    --sky-amber: #d99a2c;
    --sand-brown: #6d5a45;
    --sand-dark: #3e3327;
    --wash: rgba(255, 255, 255, 0.82);
    --white-text: #ffffff;
  }
  * { box-sizing: border-box; margin: 0; padding: 0; }
  html, body {
    width: 1200px; height: 494px; overflow: hidden;
    background: var(--paper);
    font-family: "Source Sans 3", "Myriad Pro", Arial, sans-serif;
    color: var(--ink);
  }
  .sheet { position: relative; width: 1200px; height: 494px; }

  .brand {
    position: absolute; top: 30px;
    display: flex; align-items: center; gap: 8px;
    font-weight: 700; font-size: 24px; color: var(--ink);
  }
  .brand-dot { width: 16px; height: 16px; border-radius: 50%; background: var(--sun-gold); }
  .brand--front { left: 45px; }
  .brand--back { left: 687px; }

  .postage-box {
    position: absolute; left: 396px; top: 11px; width: 91px; height: 94px;
    border: 1px solid var(--ink); background: var(--paper);
    padding: 30px 0 0 20px; font-size: 14px; line-height: 20px;
  }

  .card { position: absolute; top: 104px; width: 560px; height: 330px; overflow: hidden; }
  .card--front { left: 0; }
  .card--back { left: 640px; }

  .scene {
    position: absolute; inset: 0;
    background:
      radial-gradient(circle at 290px 70px, var(--sun-light) 0, var(--sun-gold) 90px, rgba(217,154,44,0) 200px),
      linear-gradient(180deg, var(--sky-amber) 0%, #e2b257 38%, var(--sand-brown) 62%, var(--sand-dark) 100%);
  }
  .card--front .scene-lift {
    position: absolute; left: 130px; top: 0; width: 356px; height: 100%;
    background: rgba(255, 255, 255, 0.12);
  }
  .card--back .scene { opacity: 0.35; }
  .card--back .text-panel {
    position: absolute; left: 0; top: 0; width: 323px; height: 100%;
    background: var(--wash);
  }

  .edge-band { position: absolute; right: 0; top: 0; width: 74px; height: 100%; background: var(--band); }

  .headline {
    position: absolute; left: 150px; top: 62px;
    font-family: "Dancing Script", cursive;
    font-size: 38px; font-weight: 600; color: var(--ink);
    white-space: nowrap;
  }
  .web { position: absolute; left: 22px; bottom: 12px; font-size: 13px; }
  .card--front .web { color: var(--white-text); }

  .program-title {
    position: absolute; left: 42px; top: 14px;
    font-size: 21px; font-weight: 600;
  }
  .program-sub {
    position: absolute; right: 255px; top: 42px;
    font-size: 14px; font-style: italic;
  }
  .program-body {
    position: absolute; left: 42px; top: 64px; width: 280px;
    font-size: 12.5px; line-height: 16.5px;
  }
  .program-body p + p { margin-top: 16px; }
  .program-body strong { font-weight: 700; }
  .program-body .big { font-size: 16px; }

  .side-label {
    position: absolute; top: 460px; font-size: 23px; letter-spacing: 0.5px;
  }
  .side-label--front { left: 180px; }
  .side-label--back { left: 870px; }
</style>
</head>
<body>
<div class="sheet">
  <div class="brand brand--front"><span class="brand-dot"></span>TRK Kestrel</div>
  <div class="postage-box">Postage<br>Area</div>

  <section class="card card--front">
    <div class="scene" role="img" aria-label="Sunset beach volleyball scene with silhouetted players and a net"></div>
    <div class="scene-lift"></div>
    <h1 class="headline">Beach Doubles Program</h1>
    <div class="edge-band"></div>
    <div class="web">trkkestrel.com</div>
  </section>

  <div class="brand brand--back"><span class="brand-dot"></span>TRK Kestrel</div>

  <section class="card card--back">
    <div class="scene" role="img" aria-label="Faded sunset beach scene with a volleyball player silhouette"></div>
    <div class="text-panel"></div>
    <h2 class="program-title">Training program</h2>
    <div class="program-sub">outdoor doubles</div>
    <div class="program-body">
      <p>Offer training from May until August. The cost ofthe program is $500 We are going to take no more than 16 players to train. Players must be serious to attend tryouts.</p>
      <p>●Tryouts will be <strong class="big">April 5th</strong>. We want serious players interested in training and competing at a high level. Season is from <strong>April</strong> (tryouts) to <strong>August 10.</strong> Uniform, tournament entry fees are covered, travel is not covered. Tryouts will be April 5th. Please check website <strong>(trkkestrel.com)</strong> for location and times. Additional tryouts dates will be announced on the website.</p>
    </div>
    <div class="edge-band"></div>
    <div class="web">trkkestrel.com</div>
  </section>

  <div class="side-label side-label--front">FRONT</div>
  <div class="side-label side-label--back">BACK</div>
</div>
</body>
</html>
```